MapleTrove shopping service flyer

We are a Korean shopping service. The attached picture explains our service. We would like to create a postcard or slightly larger sized flyer advertising our service. Front side will be graphics and back side text. For the front side, we want an updated version of the attached picture with our new logo and colours. And for the back side, create a simple design on the back side which we can enter all the text. Need font and design options.

Target Market(s)

20s and 30s females shopping for clothing (people not in Korea), shoppers are not Korean.

Industry/Entity Type

Online Shopping

Requirements
Must have
• For the front side, we want an updated version of the attached picture with our new logo and colours. And for the back side, create a simple design on the back side which we can enter all the text. Need font and design options.
Nice to have
• Little to no text on the front side.

```html
<!DOCTYPE html>
<html lang="en">
<head>
<meta charset="utf-8">
<title>MapleTrove shopping service flyer</title>
<link rel="stylesheet" href="https://fonts.googleapis.com/css2?family=Arimo:wght@400;700&family=Yellowtail&display=swap">
<style>
  :root {
    --teal: #1a9c8c;
    --teal-bright: #0e9e91;
    --ink: #0b2a25;
    --text: #111111;
    --highlight: #cfcfcb;
    --paper: #ffffff;
  }
  * { box-sizing: border-box; margin: 0; padding: 0; }
  html, body { width: 1200px; height: 1200px; overflow: hidden; background: var(--paper); }
  body { position: relative; font-family: "Arimo", Arial, sans-serif; }

  .side-label {
    position: absolute;
    font-weight: 700;
    font-size: 70px;
    line-height: 1;
    color: var(--teal);
    text-shadow: 3px 3px 0 var(--ink);
    letter-spacing: -0.5px;
  }
  .side-label--front { left: 795px; top: 283px; }
  .side-label--back { left: 32px; top: 877px; }

  .card {
    position: absolute;
    width: 725px;
    height: 483px;
    background: var(--paper);
    box-shadow: 0 0 10px rgba(0,0,0,0.35);
    overflow: hidden;
  }
  .card--front { left: 41px; top: 81px; }
  .card--back { left: 441px; top: 644px; }
  .card__art { position: absolute; inset: 0; width: 100%; height: 100%; }

  .brand {
    position: absolute;
    display: flex;
    align-items: center;
    font-weight: 700;
    color: var(--teal-bright);
  }
  .brand__dot { border-radius: 50%; background: var(--ink); flex: none; }
  .brand--hero { left: 50%; top: 244px; transform: translate(-50%, -50%); font-size: 58px; gap: 14px; }
  .brand--hero .brand__dot { width: 34px; height: 34px; }
  .brand--small { left: 34px; top: 52px; font-size: 15px; gap: 5px; }
  .brand--small .brand__dot { width: 10px; height: 10px; }

  .steps-title {
    position: absolute;
    left: 364px;
    top: 28px;
    transform: translateX(-50%);
    font-family: "Yellowtail", cursive;
    font-size: 76px;
    line-height: 1.2;
    color: var(--teal);
    text-shadow: 2px 2px 0 var(--ink);
    white-space: nowrap;
  }

  .step {
    position: absolute;
    transform: translateX(-50%);
    text-align: center;
    white-space: nowrap;
    color: var(--text);
  }
  .step__role { display: block; font-size: 19px; line-height: 22px; }
  .step__action {
    display: inline-block;
    font-weight: 700;
    font-size: 24px;
    line-height: 26px;
    padding: 0 8px;
    background: linear-gradient(to top, var(--highlight) 0 10px, transparent 10px);
  }
  .step--request { left: 193px; top: 169px; }
  .step--order { left: 543px; top: 170px; }
  .step--item { left: 544px; top: 322px; }
  .step--shipping { left: 193px; top: 320px; }
</style>
</head>
<body>

<div class="side-label side-label--front">Front Side</div>
<div class="side-label side-label--back">Back Side</div>

<section class="card card--front">
  <svg class="card__art" viewBox="0 0 1160 772" preserveAspectRatio="none" aria-hidden="true">
    <rect x="25" y="25" width="1110" height="721" fill="none" stroke="var(--teal)" stroke-width="3" stroke-dasharray="10 7"/>
    <!-- corner blobs: dark edge underneath, teal fill on top -->
    <path d="M0 0 H266 C262 110 170 185 60 178 L0 172 Z" fill="var(--ink)"/>
    <path d="M0 0 H258 C254 100 165 172 60 168 L0 164 Z" fill="var(--teal)"/>
    <path d="M0 462 C20 560 100 620 140 670 C170 705 172 740 170 772 H0 Z" fill="var(--ink)"/>
    <path d="M0 462 C15 560 92 622 132 672 C160 706 162 740 160 772 H0 Z" fill="var(--teal)"/>
    <path d="M1160 0 C1100 110 1080 200 1082 270 C1085 350 1130 410 1150 490 L1160 560 Z" fill="var(--ink)"/>
    <path d="M1160 0 C1108 110 1090 200 1092 262 C1095 340 1136 400 1154 470 L1160 520 Z" fill="var(--teal)"/>
    <path d="M848 772 C890 720 950 690 1030 682 C1100 674 1140 660 1160 640 V772 Z" fill="var(--ink)"/>
    <path d="M866 772 C905 728 962 700 1036 692 C1104 684 1142 670 1160 652 V772 Z" fill="var(--teal)"/>
    <!-- forward arrows -->
    <g>
      <path d="M92 268 L146 300 L92 334 Z" fill="var(--ink)"/>
      <path d="M89 265 L141 298 L89 330 Z" fill="var(--teal)"/>
      <path d="M143 268 L197 300 L143 334 Z" fill="var(--ink)"/>
      <path d="M140 265 L192 298 L140 330 Z" fill="var(--teal)"/>
      <path d="M194 268 L248 300 L194 334 Z" fill="var(--ink)"/>
      <path d="M191 265 L243 298 L191 330 Z" fill="var(--teal)"/>
    </g>
    <g transform="translate(985 600) rotate(-58)">
      <path d="M-26 -30 L30 2 L-26 34 Z" fill="var(--ink)"/>
      <path d="M-30 -33 L26 -1 L-30 31 Z" fill="var(--teal)"/>
      <path d="M26 -30 L82 2 L26 34 Z" fill="var(--ink)"/>
      <path d="M22 -33 L78 -1 L22 31 Z" fill="var(--teal)"/>
      <path d="M78 -30 L134 2 L78 34 Z" fill="var(--ink)"/>
      <path d="M74 -33 L130 -1 L74 31 Z" fill="var(--teal)"/>
    </g>
  </svg>
  <div class="brand brand--hero"><span class="brand__dot"></span>MapleTrove</div>
</section>

<section class="card card--back">
  <svg class="card__art" viewBox="0 0 1160 772" preserveAspectRatio="none" aria-hidden="true">
    <rect x="25" y="25" width="1110" height="721" fill="none" stroke="var(--teal)" stroke-width="3" stroke-dasharray="10 7"/>
    <path d="M1160 0 C1100 110 1080 200 1082 270 C1085 350 1130 410 1150 490 L1160 560 Z" fill="var(--ink)"/>
    <path d="M1160 0 C1108 110 1090 200 1092 262 C1095 340 1136 400 1154 470 L1160 520 Z" fill="var(--teal)"/>
    <path d="M848 772 C890 720 950 690 1030 682 C1100 674 1140 660 1160 640 V772 Z" fill="var(--ink)"/>
    <path d="M866 772 C905 728 962 700 1036 692 C1104 684 1142 670 1160 652 V772 Z" fill="var(--teal)"/>
    <!-- step arrows -->
    <g fill="var(--teal)">
      <path d="M561 287 L588 303 L561 320 Z"/>
      <path d="M588 287 L615 303 L588 320 Z"/>
      <path d="M615 287 L642 303 L615 320 Z"/>
      <path d="M853 402 L887 402 L870 428 Z"/>
      <path d="M853 428 L887 428 L870 454 Z"/>
      <path d="M853 454 L887 454 L870 480 Z"/>
      <path d="M642 537 L615 553 L642 570 Z"/>
      <path d="M615 537 L588 553 L615 570 Z"/>
      <path d="M588 537 L561 553 L588 570 Z"/>
    </g>
  </svg>
  <div class="brand brand--small"><span class="brand__dot"></span>MapleTrove</div>
  <h1 class="steps-title">Easy Steps</h1>

  <div class="step step--request"><span class="step__role">Costumer</span><span class="step__action">Request &amp; Payment</span></div>
  <div class="step step--order"><span class="step__role">Store</span><span class="step__action">Order &amp; Purchase</span></div>
  <div class="step step--item"><span class="step__role">Store</span><span class="step__action">Item</span></div>
  <div class="step step--shipping"><span class="step__role">Costumer</span><span class="step__action">Shipping</span></div>
</section>

</body>
</html>
```